Lantern Hearthworks Business Cards

Looking to create simple business cards that highlight our unique three sided triangle fire pit design with the colors and font of our logo, listed below.

Requirements
Must have
• Looking for something simple that includes a picture of our fire pit with name, website (lanternhearthworks.com), phone number and email. Want to keep the color mostly orange and black.
• Font is gotham(medium) and orange color code is #ee6e22

```html
<!DOCTYPE html>
<html lang="en">
<head>
<meta charset="utf-8">
<title>Lantern Hearthworks Business Cards</title>
<link rel="stylesheet" href="https://fonts.googleapis.com/css2?family=Montserrat:wght@500;700&display=swap">
<style>
  :root {
    --orange: #ee6e22;
    --card: #262324;
    --card-edge: #1d1a1b;
    --backdrop: #3a3a3a;
    --white: #f4f4f4;
    --grey: #6e6c6c;
  }
  * { box-sizing: border-box; margin: 0; padding: 0; }
  html, body { width: 1200px; height: 814px; overflow: hidden; }
  body {
    background: var(--backdrop);
    font-family: "Montserrat", sans-serif;
    font-weight: 500;
    position: relative;
  }
  .card {
    position: absolute;
    top: 252px;
    width: 540px;
    height: 310px;
    background: linear-gradient(160deg, #2d2a2b 0%, var(--card) 60%, var(--card-edge) 100%);
    box-shadow: 0 12px 30px rgba(0,0,0,.45);
    overflow: hidden;
  }
  .card--front { left: 40px; }
  .card--back { left: 620px; }

  .lockup {
    display: flex;
    align-items: center;
    gap: 14px;
  }
  .lockup__dot {
    border-radius: 50%;
    background: var(--orange);
    flex: none;
  }
  .lockup__rule {
    width: 1px;
    background: #9a9a9a;
    align-self: stretch;
  }
  .lockup__name {
    color: var(--orange);
    text-transform: uppercase;
    line-height: 1.2;
  }

  .card--front .lockup {
    position: absolute;
    left: 50%; top: 50%;
    transform: translate(-50%, -50%);
    height: 70px;
  }
  .card--front .lockup__dot { width: 46px; height: 46px; }
  .card--front .lockup__name { font-size: 22px; letter-spacing: 6px; }

  .back__emblem {
    position: absolute;
    left: 70px; top: 120px;
    width: 150px; height: 150px;
    border-radius: 50%;
    background: var(--grey);
    opacity: .35;
  }
  .back__info {
    position: absolute;
    left: 290px; top: 40px;
    width: 225px;
  }
  .back__info .lockup { height: 44px; gap: 10px; }
  .back__info .lockup__dot { width: 28px; height: 28px; }
  .back__info .lockup__name { font-size: 11.5px; letter-spacing: 3px; }
  .back__rule {
    height: 1.5px;
    background: var(--white);
    margin: 14px 0 10px;
  }
  .person__name {
    color: var(--white);
    font-weight: 700;
    font-size: 17px;
  }
  .person__title {
    color: var(--orange);
    font-size: 12px;
    margin-top: 2px;
  }
  .contact { list-style: none; }
  .contact li {
    display: flex;
    align-items: center;
    gap: 8px;
    color: var(--orange);
    font-size: 11px;
    margin-bottom: 7px;
  }
  .contact svg { width: 11px; height: 11px; flex: none; fill: var(--white); }
</style>
</head>
<body>

<section class="card card--front" aria-label="Card front">
  <div class="lockup">
    <span class="lockup__dot"></span>
    <span class="lockup__rule"></span>
    <span class="lockup__name">Lantern<br>Hearthworks</span>
  </div>
</section>

<section class="card card--back" aria-label="Card back">
  <div class="back__emblem" role="img" aria-label="Large faint brand emblem"></div>

  <div class="back__info">
    <div class="lockup">
      <span class="lockup__dot"></span>
      <span class="lockup__rule"></span>
      <span class="lockup__name">Lantern<br>Hearthworks</span>
    </div>
    <div class="back__rule"></div>
    <p class="person__name">Dana Whitlock</p>
    <p class="person__title">Founder/CEO</p>
    <div class="back__rule"></div>
    <ul class="contact">
      <li>
        <svg viewBox="0 0 16 16"><path d="M1 3h14v10H1z M1 3l7 6 7-6" fill="var(--white)" stroke="#262324" stroke-width="1.2"/></svg>
        hello@lanternhearthworks.com
      </li>
      <li>
        <svg viewBox="0 0 16 16"><path d="M4 1l3 3-2 2c1 2 3 4 5 5l2-2 3 3-2 3C7 14 2 9 1 3z"/></svg>
        503-555-0147
      </li>
      <li>
        <svg viewBox="0 0 16 16"><path d="M1 6c4-4 10-4 14 0l-2 2-2-1V5H5v2L3 8z M4 9h8l2 5H2z"/></svg>
        503-555-0182
      </li>
      <li>
        <svg viewBox="0 0 16 16"><path d="M1 2h14v9H1z M6 12h4v2H6z" fill="none" stroke="var(--white)" stroke-width="1.5"/></svg>
        lanternhearthworks.com
      </li>
    </ul>
  </div>
</section>

</body>
</html>
```